QuillMark Business Cards

I need a business card designed for QuillMark. To get an idea of what we do please visit https://formvault.example/para-creadores-3

```html
<!DOCTYPE html>
<html lang="en">
<head>
<meta charset="utf-8">
<title>QuillMark Business Cards</title>
<link rel="stylesheet" href="https://fonts.googleapis.com/css2?family=Montserrat:wght@300;400;700&display=swap">
<style>
  :root {
    --page-bg: #e6e7e8;
    --card-bg: #1c1c1c;
    --accent: #e6951e;
    --ink-light: #ffffff;
    --ink-band: #2a2a2a;
    --emboss: #555555;
  }
  * { margin: 0; padding: 0; box-sizing: border-box; }
  html, body {
    width: 1048px; height: 1200px; overflow: hidden;
    background: var(--page-bg);
    font-family: "Montserrat", Arial, sans-serif;
  }
  .canvas { position: relative; width: 1048px; height: 1200px; }
  .card { position: absolute; background: var(--card-bg); width: 843px; height: 482px; }
  .card--front { left: 84px; top: 87px; }
  .card--back { left: 76px; top: 622px; }

  .brand__dot { position: absolute; border-radius: 50%; }
  .brand__name { position: absolute; font-weight: 300; white-space: nowrap; line-height: 1; }
  .brand__tagline { position: absolute; display: flex; align-items: center; font-weight: 400; white-space: nowrap; line-height: 1; }
  .brand__rule { display: block; height: 1px; flex: 1; margin-left: 4px; }

  .card--front .brand__dot { left: 221px; top: 111px; width: 60px; height: 60px; border: 2px solid var(--accent); }
  .card--front .brand__name { left: 328px; top: 112px; color: var(--ink-light); font-size: 40px; letter-spacing: 11px; }
  .card--front .brand__tagline { left: 328px; top: 158px; width: 310px; color: var(--accent); font-size: 10px; letter-spacing: 6px; }
  .card--front .brand__rule { background: var(--ink-light); }

  .person { position: absolute; right: 429px; top: 254px; text-align: right; white-space: nowrap; }
  .person__name { color: var(--accent); font-weight: 700; font-size: 42px; letter-spacing: -1.5px; line-height: 1; }
  .person__role { color: var(--ink-light); font-weight: 400; font-size: 22px; margin-top: 8px; line-height: 1.1; }
  .divider { position: absolute; left: 438px; top: 248px; width: 2px; height: 79px; background: var(--accent); }

  .contacts { position: absolute; left: 456px; top: 243px; list-style: none; }
  .contacts li { display: flex; align-items: center; height: 30px; color: var(--ink-light); font-size: 22px; font-weight: 400; white-space: nowrap; }
  .contacts svg { width: 20px; height: 20px; margin-right: 19px; fill: var(--accent); flex: none; }

  .address-band {
    position: absolute; left: 0; top: 385px; width: 100%; height: 41px;
    background: var(--accent); color: var(--ink-band);
    display: flex; align-items: center; justify-content: center;
    font-size: 22px; font-weight: 400;
  }
  .address-band svg { width: 16px; height: 22px; fill: var(--ink-band); margin-right: 8px; }

  .card--back .brand__dot { left: 130px; top: 200px; width: 110px; height: 110px; border: 3px solid var(--emboss); }
  .card--back .brand__name { left: 293px; top: 216px; color: var(--emboss); font-size: 58px; letter-spacing: 16px; }
  .card--back .brand__tagline { left: 293px; top: 284px; width: 442px; color: var(--emboss); font-size: 13px; letter-spacing: 8px; }
  .card--back .brand__rule { background: var(--emboss); }
</style>
</head>
<body>
<main class="canvas">
  <section class="card card--front" aria-label="Business card front">
    <span class="brand__dot"></span>
    <span class="brand__name">QUILLMARK</span>
    <div class="brand__tagline">DIGITAL NOTARY<span class="brand__rule"></span></div>

    <div class="person">
      <div class="person__name">DANIEL HART</div>
      <div class="person__role">Managing Director</div>
    </div>
    <span class="divider"></span>

    <ul class="contacts">
      <li>
        <svg viewBox="0 0 24 24" aria-hidden="true"><path d="M6.62 10.79a15.05 15.05 0 0 0 6.59 6.59l2.2-2.2a1 1 0 0 1 1.02-.24 11.4 11.4 0 0 0 3.57.57 1 1 0 0 1 1 1V20a1 1 0 0 1-1 1A17 17 0 0 1 3 4a1 1 0 0 1 1-1h3.5a1 1 0 0 1 1 1c0 1.25.2 2.45.57 3.57a1 1 0 0 1-.25 1.02z"/></svg>
        044-555 010 234
      </li>
      <li>
        <svg viewBox="0 0 24 24" aria-hidden="true"><path d="M2 5h20v14H2z M3 6l9 7 9-7" fill="none" stroke="#e6951e" stroke-width="2"/></svg>
        hello@quillmark.example
      </li>
      <li>
        <svg viewBox="0 0 24 24" aria-hidden="true"><circle cx="12" cy="12" r="10"/><path d="M2 12h20M12 2c3 3 3 17 0 20M12 2c-3 3-3 17 0 20" fill="none" stroke="#1c1c1c" stroke-width="1.5"/></svg>
        www.quillmark.example
      </li>
    </ul>

    <div class="address-band">
      <svg viewBox="0 0 16 22" aria-hidden="true"><path d="M8 0a8 8 0 0 0-8 8c0 6 8 14 8 14s8-8 8-14a8 8 0 0 0-8-8zm0 11a3 3 0 1 1 0-6 3 3 0 0 1 0 6z"/></svg>
      421, Address line here&nbsp; Country Name, 45452
    </div>
  </section>

  <section class="card card--back" aria-label="Business card back">
    <span class="brand__dot"></span>
    <span class="brand__name">QUILLMARK</span>
    <div class="brand__tagline">DIGITAL NOTARY<span class="brand__rule"></span></div>
  </section>
</main>
</body>
</html>
```